New Business and Accounting Software need a Web Site

The website is for a Business and Accounting Software that has 8 products.
Each product has its owns logo and color, when you do the design have in consideration that we are looking the experience that when you change from one product page to another the look and feel adjust to the color and logo of the product.
The product are:
Ventas (Sales)
Compras (Purchases)
Contabilidad (Accounting)
Presupuesto (Budget)
Inventarios (Inventory)
Bancos (Banks)
NĂ³mina RH (Human Resources Payroll)
CRM (Customer Relationship Manager)

You can see how the main logo and variations are used in each page
- https://www.vemu.com/
- https://www.lari.com/
- https://www.tovimal.com/

Our goal is to be similar to them.

I have created a word document to explain what I want.
You need to design:
1 Home Page
1 Product Landing Page
1 Product Detail Page
1 Price Page

I am attaching:
1. Main Logo
2. 8 Product Logos
3. Website Idea, you can create your own idea.

You are welcome to use other icons for the each product if you want.

Independet professionals and Small and Medium Companies

Business and Accounting Software

Coded - Design and coding required

0054AA
0677BA
7BADD7
CADEEF
E8F1F8

• Must show all products in the main page

```html
<!DOCTYPE html>
<html lang="es">
<head>
<meta charset="utf-8">
<title>Norvo — Software de Negocios y Contabilidad</title>
<link rel="stylesheet" href="https://fonts.googleapis.com/css2?family=Questrial&family=Lato:wght@400;700&family=Lexend:wght@500;600&display=swap">
<style>
:root{
  --blue:#0054AA;
  --blue-2:#0677BA;
  --blue-light:#7BADD7;
  --blue-pale:#CADEEF;
  --blue-mist:#E8F1F8;
  --orange:#D03E1F;
  --ink:#2b2b2b;
  --muted:#555;
  --panel:#F3F5F8;
}
*{box-sizing:border-box;margin:0;padding:0}
html,body{width:1200px;height:3829px;overflow:hidden}
body{position:relative;background:#fff;font-family:Lato,sans-serif;color:var(--ink)}
.abs{position:absolute}
.btn{position:absolute;display:flex;align-items:center;justify-content:center;border-radius:22px;font-family:Questrial,sans-serif;font-size:13px;color:#fff}
.btn--dark{background:var(--blue)}
.btn--light{background:var(--blue-light)}
.btn--mist{background:var(--blue-pale);color:var(--blue)}

/* header */
.brand{display:flex;align-items:center;gap:10px;font-family:Questrial,sans-serif;font-size:40px;color:var(--blue)}
.brand__dot{width:52px;height:52px;border-radius:50%;background:var(--blue-2)}
.nav{position:absolute;top:38px;left:442px;display:flex;gap:38px;font-family:Questrial,sans-serif;font-size:13px;color:#222}
.nav a{color:inherit;text-decoration:none;padding-bottom:4px}
.nav a.is-active{border-bottom:2px solid var(--blue)}

/* hero */
.hero{top:100px;left:0;width:1200px;height:681px;background:linear-gradient(120deg,#e7e2dc 0%,#d9cfc4 45%,#9a7c6a 70%,#cfc4b9 100%)}
.hero__title{top:392px;left:76px;font-family:Questrial,sans-serif;font-size:33px;line-height:37px;color:#1f64b8}
.hero__dots{top:676px;left:76px;font-family:Questrial,sans-serif;font-size:12px;color:#333}
.dot{position:absolute;width:8px;height:8px;border-radius:50%;background:#333;top:28px}

/* section headings */
.h2{position:absolute;left:0;width:1200px;text-align:center;font-family:Questrial,sans-serif;color:#333}

/* products */
.product{position:absolute;width:260px;text-align:center;font-family:Lexend,sans-serif;font-weight:600;font-size:33px;letter-spacing:1px;color:var(--blue)}
.product__icon{margin:0 auto 14px;border-radius:14px}

/* profile cards */
.card{position:absolute;height:305px;padding:42px 18px 0 18px;color:#fff}
.card h3{font-family:Questrial,sans-serif;font-weight:400;font-size:32px}
.card h3::after{content:"";display:block;width:40px;height:2px;background:#fff;margin:14px 0 22px}
.card p{font-size:12px;line-height:22px}
.card .link{position:absolute;bottom:26px;left:26px;font-size:12px;text-decoration:underline}
.photo{position:absolute}

/* tabs */
.tab{position:absolute;top:2155px;height:58px;border-radius:10px 10px 0 0;display:flex;align-items:center;justify-content:center;font-family:Questrial,sans-serif;font-size:19px;color:#fff}
.accounts{top:2212px;left:0;width:1200px;height:565px;background:var(--panel)}
.checks{position:absolute;left:76px;top:2330px;width:470px;list-style:none}
.checks li{position:relative;padding-left:46px;font-size:12px;line-height:22px;color:#444;margin-bottom:14px}
.checks svg{position:absolute;left:0;top:0}

/* features */
.feature{position:absolute;top:2870px;width:250px;height:266px;padding:8px 24px;color:#fff;border-radius:14px 14px 14px 60px}
.feature b{display:block;font-family:Lexend,sans-serif;font-size:84px;line-height:96px;font-weight:600}
.feature h4{font-family:Questrial,sans-serif;font-weight:400;font-size:24px;margin:4px 0 14px}
.feature p{font-size:12px;line-height:22px;opacity:.9}

/* cta */
.cta{top:3240px;left:0;width:1200px;height:484px;background:var(--blue)}
.cta__title{top:3410px;left:114px;font-family:Questrial,sans-serif;font-size:35px;line-height:42px;color:#fff}

/* footer */
.subscribe{top:3757px;left:384px;width:506px;height:46px;border-radius:23px;background:#F1F3F6;font-size:12px;color:#444;padding:16px 18px}
</style>
</head>
<body>

<header>
  <div class="abs brand" style="top:20px;left:76px"><span class="brand__dot"></span>norvo</div>
  <nav class="nav"><a class="is-active">Inico</a><a>Soluciones</a><a>Planes</a><a>Contacto</a></nav>
  <a class="btn btn--dark" style="top:27px;left:848px;width:134px;height:40px">Get A Quote</a>
  <a class="btn btn--light" style="top:27px;left:992px;width:134px;height:40px">Free Trial</a>
</header>

<section>
  <div class="abs hero" role="img" aria-label="Mujer trabajando con una laptop y una calculadora en su escritorio"></div>
  <svg class="abs" style="top:690px;left:0" width="1200" height="100" viewBox="0 0 1200 100">
    <polygon points="0,91 440,75 1200,0 1200,100 0,100" fill="#fff"/>
    <line x1="440" y1="70" x2="1200" y2="16" stroke="var(--blue)" stroke-width="18" stroke-linecap="round"/>
    <line x1="808" y1="62" x2="1200" y2="36" stroke="var(--blue-light)" stroke-width="18" stroke-linecap="round"/>
  </svg>
  <h1 class="abs hero__title" style="font-weight:400">Take More Control<br>of Your Business</h1>
  <a class="btn btn--dark" style="top:482px;left:76px;width:134px;height:40px">Free Trial</a>
  <div class="abs hero__dots">02
    <span class="dot" style="left:0"></span><span class="dot" style="left:22px"></span><span class="dot" style="left:44px"></span><span class="dot" style="left:66px"></span>
  </div>
</section>

<h2 class="h2" style="top:866px;font-size:36px;font-weight:400">Adquiere solo el PLAN que necesitas</h2>

<section>
  <div class="product" style="top:938px;left:18px"><div class="product__icon" role="img" aria-label="Icono de Ventas" style="width:90px;height:96px;background:linear-gradient(45deg,#e2552a,#f4a62a)"></div>VENTAS</div>
  <div class="product" style="top:938px;left:283px"><div class="product__icon" role="img" aria-label="Icono de Compras" style="width:96px;height:90px;background:linear-gradient(160deg,var(--blue-2),var(--blue-pale))"></div>COMPRAS</div>
  <div class="product" style="top:938px;left:572px;width:260px"><div class="product__icon" role="img" aria-label="Icono de Contabilidad" style="width:110px;height:90px;background:linear-gradient(45deg,#b05ac6,#8a6ee0)"></div>CONTABILIDAD</div>
  <div class="product" style="top:938px;left:878px"><div class="product__icon" role="img" aria-label="Icono de Inventarios" style="width:88px;height:94px;background:linear-gradient(45deg,#c7283b,#f07a7a)"></div>INVENTARIOS</div>

  <div class="product" style="top:1138px;left:20px"><div class="product__icon" role="img" aria-label="Icono de Bancos" style="width:80px;height:84px;background:linear-gradient(#8d8d8d,#444)"></div>BANCOS</div>
  <div class="product" style="top:1126px;left:285px;width:300px"><div class="product__icon" role="img" aria-label="Icono de Presupuesto" style="width:170px;height:100px;background:linear-gradient(#24b08a,#0f7a6a);border-radius:85px 85px 14px 14px"></div>PRESUPUESTO</div>
  <div class="product" style="top:1134px;left:627px"><div class="product__icon" role="img" aria-label="Icono de Nómina RH" style="width:124px;height:92px;background:linear-gradient(#7fd4c8,#2aa69a);border-radius:62px 62px 14px 14px"></div>NÓMINA RH</div>
  <div class="product" style="top:1146px;left:901px"><div class="product__icon" role="img" aria-label="Icono de CRM" style="width:124px;height:80px;background:linear-gradient(#6a7fdc,#3c49b8);border-radius:62px 62px 14px 14px"></div>CRM</div>
</section>

<h2 class="h2" style="top:1348px;font-size:32px;font-weight:400;font-family:Lato,sans-serif">¿Cuál es tu perfil?</h2>

<section>
  <article class="card" style="top:1436px;left:76px;width:250px;background:var(--blue)">
    <h3>Profesional</h3>
    <p>Lorem Ipsum is simply dummy text of the printing and typesetting industry has been the industry's standard text ever since the 1500s,</p>
    <a class="btn btn--light" style="top:222px;left:16px;width:154px;height:38px;font-family:Lato,sans-serif;font-size:12px">Mas informacion</a>
  </article>
  <div class="photo" role="img" aria-label="Hombre sonriente al teléfono frente a una laptop" style="top:1436px;left:326px;width:274px;height:305px;background:linear-gradient(135deg,#7a6a5c,#dfe4ea 55%,#8fa4c0)"></div>

  <article class="card" style="top:1436px;left:626px;width:250px;background:var(--blue-light)">
    <h3>Contador</h3>
    <p>Lorem Ipsum is simply dummy text of the printing and typesetting industry has been the industry's standard text ever since the 1500s,</p>
    <a class="btn btn--dark" style="top:222px;left:12px;width:154px;height:38px;font-family:Lato,sans-serif;font-size:12px">Mas informacion</a>
  </article>
  <div class="photo" role="img" aria-label="Mujer con lentes revisando documentos con calculadora" style="top:1436px;left:876px;width:250px;height:305px;background:linear-gradient(135deg,#5a4a3f,#e6e2dc 55%,#b9b2a8)"></div>

  <article class="card" style="top:1768px;left:76px;width:250px;background:var(--blue-light)">
    <h3>Micro</h3>
    <p>Lorem Ipsum is simply dummy text of the printing and typesetting industry has been the industry's standard dummy text ever since the 1500s,</p>
    <span class="link">Mas informacion</span>
  </article>
  <article class="card" style="top:1768px;left:350px;width:250px;background:var(--blue)">
    <h3>Micro</h3>
    <p>Lorem Ipsum is simply dummy text of the printing and typesetting industry has been the industry's standard dummy text ever since the 1500s,</p>
    <span class="link">Mas informacion</span>
  </article>
  <article class="card" style="top:1768px;left:626px;width:250px;background:var(--orange)">
    <h3>Empresarial</h3>
    <p>Lorem Ipsum is simply dummy text of the printing and typesetting industry has been the industry's standard dummy text ever since the 1500s,</p>
    <span class="link">Mas informacion</span>
  </article>
  <div class="photo" role="img" aria-label="Equipo reunido alrededor de una mesa vista desde arriba" style="top:1768px;left:876px;width:250px;height:305px;background:linear-gradient(90deg,#d9d4cc,#6b4a36 45%,#6b4a36 55%,#d9d4cc)"></div>
</section>

<section>
  <div class="tab" style="left:76px;width:314px;background:#f1f2f4;color:#333">Get Smart Chart of Accounts</div>
  <div class="tab" style="left:407px;width:191px;background:var(--blue-light)">Tab 2</div>
  <div class="tab" style="left:612px;width:192px;background:var(--blue)">Tab 3</div>
  <div class="tab" style="left:819px;width:192px;background:var(--orange)">Tab 4</div>
  <div class="abs accounts"></div>
  <h3 class="abs" style="top:2276px;left:78px;font-family:Questrial,sans-serif;font-weight:400;font-size:31px;color:#222">Get Smart Chart of Accounts</h3>
  <ul class="checks">
    <li><svg width="30" height="26" viewBox="0 0 30 26"><circle cx="13" cy="13" r="11" fill="none" stroke="var(--blue)" stroke-width="2.5"/><path d="M7 13l5 5L28 3" fill="none" stroke="var(--blue)" stroke-width="3"/></svg>Lorem Ipsum is simply dummy text of the printing and typesetting industry has been the industry's.</li>
    <li style="margin-top:20px"><svg width="30" height="26" viewBox="0 0 30 26"><circle cx="13" cy="13" r="11" fill="none" stroke="var(--blue)" stroke-width="2.5"/><path d="M7 13l5 5L28 3" fill="none" stroke="var(--blue)" stroke-width="3"/></svg>Lorem Ipsum is simply dummy text of the printing and typesetting industry has been the industry's standard dummy text ever since the 1500s,</li>
    <li><svg width="30" height="26" viewBox="0 0 30 26"><circle cx="13" cy="13" r="11" fill="none" stroke="var(--blue)" stroke-width="2.5"/><path d="M7 13l5 5L28 3" fill="none" stroke="var(--blue)" stroke-width="3"/></svg>Lorem Ipsum is simply dummy text of the printing and typesetting industry has been the industry's standard dummy text ever since the 1500s,</li>
    <li style="margin-top:16px"><svg width="30" height="26" viewBox="0 0 30 26"><circle cx="13" cy="13" r="11" fill="none" stroke="var(--blue)" stroke-width="2.5"/><path d="M7 13l5 5L28 3" fill="none" stroke="var(--blue)" stroke-width="3"/></svg>Lorem Ipsum is simply dummy text of the printing and typesetting industry has been the industry's.</li>
  </ul>
  <a class="btn btn--dark" style="top:2646px;left:76px;width:154px;height:38px;font-family:Lato,sans-serif;font-size:12px">Mas informacion</a>
  <div class="photo" role="img" aria-label="Manos escribiendo en una laptop con un plan de cuentas en pantalla" style="top:2272px;left:610px;width:481px;height:436px;border-radius:14px 60px 14px 90px;background:linear-gradient(135deg,#e9ecef,#bfc6cc 45%,#f2f2f2 70%,#d9b24a)"></div>
</section>

<section>
  <div class="feature" style="left:78px;background:var(--blue-light)"><b>1.</b><h4>Paga por uso</h4><p>Lorem Ipsum is simply dummy text of the printing and typesetting.</p></div>
  <div class="feature" style="left:344px;background:var(--blue)"><b>2.</b><h4>Sin Contrato</h4><p>Lorem Ipsum is simply dummy text of the printing and typesetting.</p></div>
  <div class="feature" style="left:610px;background:var(--orange)"><b>3.</b><h4>En La Nube</h4><p>Lorem Ipsum is simply dummy text of the printing and typesetting.</p></div>
  <div class="feature" style="left:876px;background:#000"><b>4.</b><h4 style="font-size:21px">Multiples Dispositivos</h4><p>Lorem Ipsum is simply dummy text of the printing and typesetting.</p></div>
</section>

<section>
  <div class="abs cta"></div>
  <div class="photo" role="img" aria-label="Mano con bolígrafo sobre una calculadora y gráficos financieros" style="top:3180px;left:600px;width:490px;height:450px;border-radius:70px 90px 90px 90px;background:linear-gradient(135deg,#ffffff,#c8cdd6 40%,#7a8290 60%,#e8ecf2)"></div>
  <h2 class="abs cta__title" style="font-weight:400">?Que Esperas Para Crear<br>Una Cuenta Gratis En<br>Norvo?</h2>
  <a class="btn btn--light" style="top:3555px;left:110px;width:170px;height:38px;font-family:Lato,sans-serif;font-size:12px">Crear Cuenta Gratis</a>
</section>

<footer>
  <div class="abs brand" style="top:3752px;left:76px"><span class="brand__dot"></span>norvo</div>
  <div class="abs subscribe">Reciba Las actualizaciones de Norvo</div>
  <a class="btn btn--dark" style="top:3757px;left:912px;width:214px;height:46px;font-family:Lato,sans-serif">Suscribirme</a>
</footer>

</body>
</html>
```